Humorous Book by Comedian Needs E-book Cover

My book 'A Kettle on the Porch' is on Leafpad but I want a better cover designed. Cover needs my photo on it. My name is the most important text (because I have an existing audience.)

Text elements:
Author: Dorvel Pim
Title: A Kettle on the Porch
Subtitle: Tenth Anniversary Edition
Review Quote: 'All of his columns are amusing. The best are masterpieces.' Harbour Ledger

Above my name it should say: Collected Humour From NZ's Award-Winning Comedian

Here's the present version (which is why I want an improved version!)
http://www.brightmart-example.com/A-Kettle-Porch-Anniversary-Edition-ebook/dp/Q77TX2M904

Book covers I admire:

http://www.brightmart-example.co.uk/Why-The-Fern-Odile-Brask-ebook/dp/Q3318ZR7LN/ref=tmm_kin_title_0

http://www.brightmart-example.com/Gravelhat-Mira-Dunst-ebook/dp/Q691PLE583/ref=tmm_kin_title_0

http://www.brightmart-example.co.uk/Why-Keep-Lantern-Rex-Palfrey-ebook/dp/Q58JN3TQ7V

Leafpad covers need to work as thumbnails, as well as on small device screens.

This cover is for Brightmart Leafpad. Tech specs are on Leafpad Direct Publishing page. Dimensions: Requirements for the size of your cover art have an ideal height/width ratio of 1.6, this means: • A minimum of 625 pixels on the shortest side and 1000 pixels on the longest side • For best quality, your image would be 2820 pixels on the shortest side and 4500 pixels on the longest side

Dimensions Requirements for the size of your cover art have an ideal height/width ratio of 1.6, this means: • A minimum of 625 pixels on the shortest side and 1000 pixels on the longest side • For best quality, your image would be 2820 pixels on the shortest side and 4500 pixels on the longest side

Comedian

```html
<!DOCTYPE html>
<html lang="en">
<head>
<meta charset="utf-8">
<title>A Kettle on the Porch — Dorvel Pim</title>
<link rel="stylesheet" href="https://fonts.googleapis.com/css2?family=Questrial&family=Jost:wght@600&family=Arimo:wght@400&display=swap">
<style>
  :root {
    --orange-deep: #f27a12;
    --orange-mid: #f7902a;
    --orange-glow: #ffd9a8;
    --ink: #2b2b2b;
    --ink-soft: #3d3d3d;
    --white: #ffffff;
    --band: rgba(255, 236, 214, 0.55);
    --suit-light: #f4efd2;
    --suit-shade: #ddd5ae;
    --skin: #c88d68;
    --hair: #2a2320;
  }
  html, body {
    margin: 0;
    padding: 0;
    overflow: hidden;
    background: #ffffff;
  }
  p, h1, h2 { margin: 0; }
  .cover {
    position: relative;
    width: 750px;
    height: 1200px;
    overflow: hidden;
    background:
      radial-gradient(ellipse 330px 420px at 375px 560px, var(--orange-glow) 0%, var(--orange-mid) 55%, var(--orange-deep) 100%);
    font-family: 'Arimo', Arial, sans-serif;
  }
  .kicker {
    position: absolute;
    top: 77px;
    left: 0;
    width: 100%;
    text-align: center;
    color: var(--white);
    font-size: 25px;
    line-height: 1;
    letter-spacing: 1.3px;
    white-space: nowrap;
  }
  .author {
    position: absolute;
    top: 120px;
    left: 0;
    width: 100%;
    text-align: center;
    font-family: 'Questrial', 'Century Gothic', sans-serif;
    font-weight: 400;
    font-size: 96px;
    line-height: 1;
    letter-spacing: 13px;
    white-space: nowrap;
  }
  .author-first { color: var(--white); }
  .author-last { color: var(--ink); }
  .author-photo {
    position: absolute;
    left: 0;
    top: 0;
    width: 750px;
    height: 1200px;
  }
  .review {
    position: absolute;
    top: 400px;
    left: 498px;
    width: 240px;
    text-align: center;
    color: var(--ink);
  }
  .review-quote {
    font-size: 25px;
    line-height: 30px;
    letter-spacing: 1.5px;
  }
  .review-source {
    margin-top: 30px;
    font-size: 15px;
    line-height: 1;
    letter-spacing: 0.5px;
  }
  .title-band {
    position: absolute;
    top: 760px;
    left: 0;
    width: 100%;
    height: 104px;
    background: var(--band);
  }
  .title {
    position: absolute;
    top: 788px;
    left: 0;
    width: 100%;
    text-align: center;
    font-family: 'Jost', 'Futura', sans-serif;
    font-weight: 600;
    font-size: 60px;
    line-height: 1.1;
    letter-spacing: 4px;
    color: var(--ink-soft);
    white-space: nowrap;
  }
  .edition {
    position: absolute;
    top: 1156px;
    left: 0;
    width: 100%;
    text-align: center;
    font-size: 26px;
    line-height: 1;
    letter-spacing: 2.5px;
    color: #111111;
  }
</style>
</head>
<body>
  <main class="cover">
    <p class="kicker">Collected Humour from NZ's Award-Winning Comedian</p>
    <h1 class="author"><span class="author-first">DORVEL</span> <span class="author-last">PIM</span></h1>

    <svg class="author-photo" viewBox="0 0 750 1200" role="img" aria-label="Photo of the author, smiling, wearing glasses, a cream dinner jacket and a navy bow tie, adjusting his cuff">
      <defs>
        <linearGradient id="suitTone" x1="0" y1="0" x2="1" y2="1">
          <stop offset="0" stop-color="var(--suit-light)"/>
          <stop offset="1" stop-color="var(--suit-shade)"/>
        </linearGradient>
        <linearGradient id="headTone" x1="0" y1="0" x2="0" y2="1">
          <stop offset="0" stop-color="var(--hair)"/>
          <stop offset="0.28" stop-color="var(--skin)"/>
          <stop offset="1" stop-color="var(--skin)"/>
        </linearGradient>
      </defs>
      <path d="M248 300 Q250 236 350 236 Q462 236 470 320 L468 520 Q440 600 360 606 Q270 600 250 520 Z" fill="url(#headTone)"/>
      <path d="M60 1200 L46 820 Q50 690 160 650 L290 600 Q360 640 430 600 L560 650 Q660 690 690 820 L712 1200 Z" fill="url(#suitTone)"/>
    </svg>

    <aside class="review">
      <p class="review-quote">'All of his columns are amusing. The best are masterpieces.'</p>
      <p class="review-source">Harbour Ledger</p>
    </aside>

    <div class="title-band"></div>
    <h2 class="title">A Kettle on the Porch</h2>

    <p class="edition">Tenth Anniversary Edition</p>
  </main>
</body>
</html>
```